www.HarborviewSmileGlow.com needs to be re-designed

Current website to be redesigned www.HarborviewSmileGlow.com

*Need a custom-made new theme

I need all 10 pages redesigned using existing content.
I need the website to be revamped to a more modern look.

Please start with Homepage first then after homepage mock up is approved we can move forward with rest of pages.

Please use existing images from my Facebook or Instagram page of our real customers for banner image...

(Where to find my FB and IG pages...
You can access these pages from the website header and "contact us" page for address.)

I would like to have a button that says "Book Appointment Online" and get rid of the actual form that is on current website.

But other than that please include all other content, features, etc in mock ups so I can make a decision on the website.

I prefer custom design and must be WP installable responsive theme.

This is design-only. I am open to any concepts you can submit.

Target Market(s)

people that care about thier looks

Industry/Entity Type

Dental Clinic

Colors

Designer to choose colors to be used in the design.

Requirements
Must have
• All current content/text that is currently on website. Just formatted so it doesnt look so busy. I want to make emphasis on BOOK APPOINTMENT button and $99 SPECIAL BUTTON
Nice to have
• White background so everything pops
Should not have
• I do not like stock photo images, please use images from my facebook and IG page of real customers or even a snap shot of our office building. You can access these pages from the website header and contact us page for address, maybe yu can use snapshot somewhere of building of our address on homepage possibly in banner image.

```html
<!DOCTYPE html>
<html lang="en">
<head>
<meta charset="utf-8">
<title>Harborview Smile Glow</title>
<link href="https://fonts.googleapis.com/css2?family=Poppins:wght@300;400;500;600;700&display=swap" rel="stylesheet">
<style>
:root{
  --cyan:#1fc6ee;
  --cyan-deep:#14a9d4;
  --ink:#111111;
  --text:#555555;
  --muted:#8a8a8a;
  --soft:#f5f5f5;
  --line:#dcdcdc;
  --panel:#3c3c3c;
  --white:#ffffff;
}
*{box-sizing:border-box;margin:0;padding:0}
html,body{width:1200px;height:3758px;overflow:hidden}
body{font-family:'Poppins',sans-serif;color:var(--text);background:var(--white);position:relative}
a{text-decoration:none}
section,header,nav,footer{position:absolute;left:0;width:1200px}
.btn{display:inline-flex;align-items:center;justify-content:center;gap:10px;background:var(--ink);color:var(--white);font-weight:600;border-radius:8px;white-space:nowrap}
.btn-icon{width:22px;height:22px;border:2px solid var(--cyan);border-radius:3px;position:relative;flex:none}
.btn-icon::after{content:"";position:absolute;left:3px;right:3px;top:4px;height:2px;background:var(--cyan)}

/* header */
.site-header{top:0;height:117px}
.header-phone{position:absolute;left:195px;top:52px;display:flex;align-items:center;gap:10px;font-size:15px;font-weight:600;color:var(--ink)}
.brand{position:absolute;left:490px;top:34px;width:230px;display:flex;align-items:center;gap:10px}
.brand-mark{width:46px;height:46px;border-radius:50%;background:#e6e6e6;flex:none}
.brand-name{font-size:19px;font-weight:500;color:var(--panel);line-height:1.1}
.header-book{position:absolute;left:817px;top:42px;width:205px;height:50px;font-size:14px}

.main-nav{top:117px;height:51px;background:var(--cyan);display:flex;justify-content:center;align-items:center;gap:26px}
.main-nav a{color:var(--white);font-size:13px;font-weight:600}

/* hero */
.hero{top:168px;height:497px;background:var(--soft)}
.hero-photo{position:absolute;right:0;top:0;width:450px;height:497px;background:linear-gradient(135deg,#e9d3b4 0%,#d9b48e 45%,#f3eee8 100%)}
.hero-dots{position:absolute;left:45px;top:235px;display:flex;flex-direction:column;gap:12px}
.hero-dots span{width:13px;height:13px;border-radius:50%;background:var(--cyan)}
.hero-dots span:first-child{background:var(--ink)}
.hero-title{position:absolute;left:195px;top:105px;width:520px;font-size:34px;font-weight:600;color:var(--cyan);line-height:1.35}
.hero-list{position:absolute;left:197px;top:240px;list-style:none}
.hero-list li{display:flex;align-items:center;gap:16px;font-size:17px;margin-bottom:8px;color:var(--text)}
.hero-book{position:absolute;left:199px;top:362px;width:205px;height:50px;font-size:14px}

/* intro */
.intro{top:665px;height:480px;text-align:center}
.section-title{font-size:32px;font-weight:600;color:var(--cyan)}
.intro .section-title{margin-top:60px}
.intro-sub{font-size:14px;margin-top:14px;color:var(--text)}
.intro-copy{width:820px;margin:42px auto 0;font-size:13.5px;line-height:1.75;color:var(--muted)}
.special-btn{position:absolute;left:475px;top:335px;width:250px;height:62px;font-size:24px;font-weight:700}
.special-btn b{color:var(--cyan)}

/* how */
.how{top:1145px;height:500px;text-align:center;background:linear-gradient(180deg,#3fd0f3 0%,#1fc6ee 55%,#22bde4 100%)}
.how .section-title{color:var(--white);margin-top:118px}
.how-copy{width:870px;margin:30px auto 0;font-size:14px;line-height:1.8;color:rgba(255,255,255,.85)}
.how-btn{position:absolute;left:536px;top:360px;width:160px;height:48px;font-size:14px}

/* testimonials */
.testimonials{top:1645px;height:605px;text-align:center}
.testimonials .section-title{margin-top:83px}
.t-card{position:absolute;top:220px;width:252px;height:300px;border:1px solid var(--line)}
.t-avatar{position:absolute;left:50%;top:-50px;margin-left:-49px;width:98px;height:98px;border-radius:50%;border:4px solid var(--cyan);background:linear-gradient(160deg,#c9a98a,#6d5a4e)}
.t-name{position:absolute;left:0;right:0;top:84px;font-size:11px;color:var(--ink);font-weight:600}
.t-name span{color:var(--muted);font-weight:400}
.t-divider{position:absolute;left:0;right:0;top:130px;border-top:1px solid var(--line)}
.t-text{position:absolute;left:22px;right:22px;top:160px;font-size:11.5px;line-height:1.7;color:var(--text)}

/* compare */
.compare{top:2250px;height:745px;background:var(--soft);text-align:center}
.compare .section-title{margin-top:72px}
.compare-sub{font-size:14px;margin-top:8px;color:var(--ink);word-spacing:4px}
.c-card{position:absolute;top:192px;width:182px;height:391px;border:2px solid var(--cyan);background:var(--white);font-size:14.5px;color:var(--text)}
.c-card .c-name{height:88px;display:flex;align-items:center;justify-content:center;font-size:20px;font-weight:600;color:#1a4a8a}
.c-card ul{list-style:none;margin-top:56px}
.c-card li{margin-bottom:22px}
.c-card.featured{border:none;background:var(--panel);color:var(--white)}
.c-card.featured .c-name{background:var(--white);font-size:15px;color:var(--panel);font-weight:500}
.compare-btn{position:absolute;left:519px;top:638px;width:160px;height:46px;background:var(--cyan);color:var(--white);border-radius:8px;font-size:14px;font-weight:600;display:flex;align-items:center;justify-content:center}

/* why */
.why{top:2995px;height:367px;text-align:center}
.why .section-title{margin-top:45px}
.why-item{position:absolute;top:165px;width:150px;margin-left:-75px;text-align:center}
.why-item svg{display:block;margin:0 auto}
.why-item p{margin-top:22px;font-size:18px;font-weight:600;color:var(--ink)}

/* footer */
.site-footer{top:3362px;height:396px;background:var(--soft)}
.footer-brand{position:absolute;left:200px;top:50px;width:190px;display:flex;align-items:center;gap:10px}
.footer-brand .brand-mark{width:38px;height:38px}
.footer-brand .brand-name{font-size:15px;line-height:1.15;width:140px}
.footer-menu{position:absolute;left:418px;top:52px;list-style:none;font-size:11.5px;color:var(--ink);line-height:1.9}
.footer-info{position:absolute;left:575px;top:50px;width:230px;font-size:11.5px;color:var(--ink);line-height:1.6}
.info-block{position:relative;padding-left:26px;margin-bottom:22px}
.info-block h4{color:var(--cyan);font-size:11.5px;font-weight:600}
.info-block svg{position:absolute;left:0;top:2px}
.footer-book{position:absolute;left:824px;top:62px;width:170px;height:42px;font-size:12px}
.footer-social{position:absolute;left:838px;top:148px;display:flex;gap:12px}
.footer-social span{width:13px;height:13px;background:var(--cyan-deep);border-radius:2px}
.copyright{position:absolute;left:0;right:0;top:352px;text-align:center;font-size:11px;color:var(--ink)}
</style>
</head>
<body>

<header class="site-header">
  <div class="header-phone">
    <svg width="20" height="20" viewBox="0 0 24 24" fill="none" stroke="#1fc6ee" stroke-width="2"><path d="M5 3h4l2 5-3 2a12 12 0 0 0 6 6l2-3 5 2v4a2 2 0 0 1-2 2A18 18 0 0 1 3 5a2 2 0 0 1 2-2z"/></svg>
    555-314-2780
  </div>
  <div class="brand"><span class="brand-mark"></span><span class="brand-name">Harborview<br>Smile Glow</span></div>
  <a class="btn header-book" href="#"><span class="btn-icon"></span>Book Appointments</a>
</header>

<nav class="main-nav">
  <a href="#">Home</a><a href="#">Our Process</a><a href="#">Photos</a><a href="#">White Smile Club</a><a href="#">Testimonials</a><a href="#">Appointments</a><a href="#">FAQ</a><a href="#">Contact</a><a href="#">Blog</a><a href="#">Buy Now</a>
</nav>

<section class="hero">
  <div class="hero-photo" role="img" aria-label="Smiling customer with bright white teeth"></div>
  <div class="hero-dots"><span></span><span></span><span></span><span></span></div>
  <h1 class="hero-title">Get That White Smile You've Always Wanted</h1>
  <ul class="hero-list">
    <li><svg width="16" height="14" viewBox="0 0 16 14"><path d="M1 7l5 5L15 1" fill="none" stroke="#1fc6ee" stroke-width="3"/></svg>Amazing Results</li>
    <li><svg width="16" height="14" viewBox="0 0 16 14"><path d="M1 7l5 5L15 1" fill="none" stroke="#1fc6ee" stroke-width="3"/></svg>The Most Effective System</li>
    <li><svg width="16" height="14" viewBox="0 0 16 14"><path d="M1 7l5 5L15 1" fill="none" stroke="#1fc6ee" stroke-width="3"/></svg>More Affordable Than The Dentist</li>
  </ul>
  <a class="btn hero-book" href="#"><span class="btn-icon"></span>Book Appointments</a>
</section>

<section class="intro">
  <h2 class="section-title">Harborview Smile Glow</h2>
  <p class="intro-sub">The best price, service and results.</p>
  <p class="intro-copy">Harborview Smile Glow features state-of-the-art technologies that are safe, industry-unique and very cost-effective. Our teeth whitening system utilizes the latest blue light whitening technology. Our Blue Light Systems are calibrated precisely for optimal activation of our exclusive hydrogen peroxide based whitening solution which is manufactured in a FDA registered facility in the USA.</p>
  <a class="btn special-btn" href="#"><b>$99</b> SPECIAL</a>
</section>

<section class="how" role="img" aria-label="Team of whitening staff smiling in the clinic, tinted cyan">
  <h2 class="section-title">How It Works</h2>
  <p class="how-copy">We have a very effective teeth whitening treatment that is guaranteed to get you quick results in about 1 hour. To start the treatment, your apply a hydrogen peroxide based whitening agent to your teeth. We then place our cold blue light directly in front of your exposed teeth for 15 minutes per treatment. The lighting systems we use activate the whitening agent and thats what accelerates the whitening process giving you whiter teeth in less than an hour.</p>
  <a class="btn how-btn" href="#">Learn More</a>
</section>

<section class="testimonials">
  <h2 class="section-title">Testimonials</h2>
  <div class="t-card" style="left:200px">
    <div class="t-avatar" role="img" aria-label="Customer portrait"></div>
    <p class="t-name">Carla M | <span>Harborview</span></p>
    <div class="t-divider"></div>
    <p class="t-text">Had a terrific experience at HSG teeth whitening center. Marisol is great, reasonably priced, I highly recommend.</p>
  </div>
  <div class="t-card" style="left:474px">
    <div class="t-avatar" role="img" aria-label="Customer portrait"></div>
    <p class="t-name">Dana R | <span>Harborview, CA</span></p>
    <div class="t-divider"></div>
    <p class="t-text">Great price, great results, easy and painless. This place was easy to find. The price was outstanding! And my teeth are at least two shades!</p>
  </div>
  <div class="t-card" style="left:746px">
    <div class="t-avatar" role="img" aria-label="Customer portrait"></div>
    <p class="t-name">Helen T | <span>Cedar Falls, Ut</span></p>
    <div class="t-divider"></div>
    <p class="t-text">Wow.. What a terrific experience! Professional, state-of-the-art equipment and Marisol is wonderful!! I will definitely be returning when I'm back in Harborview! I highly recommend this service, exceptional!</p>
  </div>
</section>

<section class="compare">
  <h2 class="section-title">Compare Us</h2>
  <p class="compare-sub">Speed &nbsp;| Ease Of Use &nbsp;| Cost &nbsp;| Availability &nbsp;| Pain</p>
  <div class="c-card" style="left:200px">
    <div class="c-name">Lumina</div>
    <ul><li>1-2 Hours</li><li>Difficult/Dentist</li><li>$300-$600</li><li>Limited Availability</li><li>Pain &amp; Sensitivity</li></ul>
  </div>
  <div class="c-card" style="left:403px">
    <div class="c-name">BrightArc</div>
    <ul><li>7-14 Days</li><li>Difficult</li><li>$300-$600</li><li>Limited Availability</li><li>Sensitivity</li></ul>
  </div>
  <div class="c-card featured" style="left:609px">
    <div class="c-name">Harborview Smile Glow</div>
    <ul><li>45 Mins</li><li>Very Easy</li><li>$378</li><li>Appt Only</li><li>No Pain</li></ul>
  </div>
  <div class="c-card" style="left:812px">
    <div class="c-name" style="color:#333">GlowKit</div>
    <ul><li>7-30 Days</li><li>Difficult</li><li>$50-$150</li><li>Store Purchase</li><li>Sensitivity</li></ul>
  </div>
  <a class="compare-btn" href="#">Compare Now</a>
</section>

<section class="why">
  <h2 class="section-title">Why Choose Us?</h2>
  <div class="why-item" style="left:275px">
    <svg width="80" height="85" viewBox="0 0 80 85" fill="none" stroke="#1fc6ee" stroke-width="3"><path d="M28 6h24l-7 14H35z"/><path d="M35 20C12 34 8 78 40 80c32-2 28-46 5-60"/><path d="M46 42c-2-4-12-4-12 2s12 4 12 10-10 6-12 2M40 36v30"/></svg>
    <p>Price</p>
  </div>
  <div class="why-item" style="left:448px">
    <svg width="70" height="85" viewBox="0 0 70 85" fill="none" stroke="#111" stroke-width="3"><rect x="5" y="10" width="60" height="72" rx="3"/><rect x="22" y="4" width="26" height="12"/><path d="M15 66l14-16 10 10 16-22M48 38h7v7"/></svg>
    <p>Results</p>
  </div>
  <div class="why-item" style="left:596px">
    <svg width="80" height="85" viewBox="0 0 80 85" fill="none" stroke="#111" stroke-width="3"><path d="M40 10c-8-6-22-2-22 10-10 2-12 16-4 22-6 10 2 24 14 22 4 10 12 10 12 0zM40 10c8-6 22-2 22 10 10 2 12 16 4 22 6 10-2 24-14 22-4 10-12 10-12 0z"/><path d="M40 10v64M26 30c6 0 8 4 8 8M54 30c-6 0-8 4-8 8M26 54c6 0 8-4 8-8M54 54c-6 0-8-4-8-8"/></svg>
    <p>No Pain</p>
  </div>
  <div class="why-item" style="left:741px">
    <svg width="80" height="85" viewBox="0 0 80 85" fill="none" stroke="#111" stroke-width="3"><circle cx="40" cy="42" r="14"/><path d="M36 8h8l2 10 8 4 9-6 6 6-6 9 4 8 10 2v8l-10 2-4 8 6 9-6 6-9-6-8 4-2 10h-8l-2-10-8-4-9 6-6-6 6-9-4-8-10-2v-8l10-2 4-8-6-9 6-6 9 6 8-4z"/></svg>
    <p>Service</p>
  </div>
  <div class="why-item" style="left:902px">
    <svg width="70" height="85" viewBox="0 0 70 85" fill="none" stroke="#111" stroke-width="3"><path d="M35 8a24 24 0 0 0-14 43c3 3 4 6 4 10h20c0-4 1-7 4-10A24 24 0 0 0 35 8z"/><path d="M26 68h18M28 76h14M38 22l-8 16h10l-8 16"/></svg>
    <p>Convenience</p>
  </div>
</section>

<footer class="site-footer">
  <div class="footer-brand"><span class="brand-mark"></span><span class="brand-name">Harborview<br>Smile Glow</span></div>
  <ul class="footer-menu">
    <li>Home</li><li>Our Process</li><li>Photos</li><li>White Smile Club</li><li>Testimonials</li><li>Appointments</li><li>FAQ</li><li>Contact</li><li>Blog</li><li>Buy Now</li>
  </ul>
  <div class="footer-info">
    <div class="info-block">
      <svg width="12" height="14" viewBox="0 0 12 14"><path d="M6 0a5 5 0 0 0-5 5c0 4 5 9 5 9s5-5 5-9a5 5 0 0 0-5-5z" fill="#111"/><circle cx="6" cy="5" r="2" fill="#f5f5f5"/></svg>
      <h4>Location</h4>
      <p>418 Marina Crest Way<br>Ste 12 | Harborview, CA 90000</p>
    </div>
    <div class="info-block">
      <svg width="13" height="13" viewBox="0 0 13 13"><circle cx="6.5" cy="6.5" r="5.5" fill="none" stroke="#111" stroke-width="2"/><path d="M6.5 3v4h3" stroke="#111" stroke-width="1.5" fill="none"/></svg>
      <h4>Opening Hours</h4>
      <p>Monday to Friday: 9am-5pm<br>Saturday: 10am-3pm</p>
    </div>
    <div class="info-block">
      <svg width="13" height="13" viewBox="0 0 24 24"><path d="M5 3h4l2 5-3 2a12 12 0 0 0 6 6l2-3 5 2v4a2 2 0 0 1-2 2A18 18 0 0 1 3 5a2 2 0 0 1 2-2z" fill="#111"/></svg>
      <h4>Phone</h4>
      <p>555-410-2231, 555-860-4417</p>
    </div>
  </div>
  <a class="btn footer-book" href="#"><span class="btn-icon"></span>Book Appointments</a>
  <div class="footer-social" aria-label="Social links"><span></span><span></span><span></span><span></span><span></span><span></span></div>
  <p class="copyright">© 2017 Company Name &nbsp;| All Rights Reserved</p>
</footer>

</body>
</html>
```